Brochure Design Project

A4 Portrait
8 Page Sales brochure for Automatic Coffee Machines for Offices.
We have 4 products in 4 cateries.
Small Office
Medium Office
Large Office
Whole Company / Food Service.

There will be a product image plus 3-4 accessories for each product

Then a brief sales pitch text for each product.

We supply to public listed companies therefore it has to be professional, well presented and eye catching.

Thank you
Updates

I will make the budget $200

Project Deadline Extended

Hello,

Please note that I've made changes to the job brief. 

Thanks

Walter 

Hi 

Please find attached contents in pdf for your implementation.

1. Small Office Solution
2. Medium Office Solution 
3. Large Office Solution
4. Whole Company Solution
5. Food Service

Thanks 

Walter

Project Deadline Extended

Hi All

Budget increased to $200, extended project by 7 more days.

Thank you

Howard Benlo

Target Market(s)

Big Corporate Companies in major Australian cities

Industry/Entity Type

It Company

Requirements
Must have
• A4 Portrait
8 Page photo and sales pitch text. One product per page starting from 3nd page
5 products into 5 categories of

Page 2 will tell about our company and services

Small Office Solution (page 3)
$16 per day)

Medium Office Solution (page 4)
$18 per day)

Large Office Solution (page 5)
$19 per day)

Whole Company (page 6)
$24 per day)

Food Service Solution (page 7
$28 per day

Each product page will highlight
eg
Small Office Solution
$16 per day)

Each page will have 3-4 accessories (photos)

Page 8 Our logo, address & Conatct details - Please see for contact details http://www.brewvanta.com.au/brew_va
Nice to have
• Logo, photo of coffee machine, an office environment where people are kind of enjoying coffee in a lounge.

Should not have
• Not messy, no old style,

```html
<!DOCTYPE html>
<html lang="en">
<head>
<meta charset="utf-8">
<title>Brewvanta – Whole Company &amp; Food Service Solutions</title>
<link rel="stylesheet" href="https://fonts.googleapis.com/css2?family=Open+Sans:wght@300;400;600;700;800&display=swap">
<style>
  :root {
    --backdrop: #2e2e30;
    --red: #d2202a;
    --red-deep: #8f0f16;
    --title-bar: #4b4b4d;
    --title-bar-dark: #333335;
    --info-bar: #3a3a3c;
    --orange: #f26a21;
    --content-bg: #e6e6e6;
    --box-bg: #ffffff;
    --ink: #2a2a2a;
    --muted: #9a9a9a;
    --white: #ffffff;
  }
  * { box-sizing: border-box; margin: 0; padding: 0; }
  html, body {
    width: 1200px; height: 793px; overflow: hidden;
    background: var(--backdrop);
    font-family: "Open Sans", Arial, sans-serif;
    color: var(--ink);
  }
  .spread {
    position: absolute; left: 77px; top: 26px;
    width: 1046px; height: 740px;
    display: flex;
  }
  .page {
    position: relative; width: 523px; height: 740px;
    background: var(--content-bg); overflow: hidden;
  }
  .band-top, .band-bottom {
    position: absolute; left: 0; right: 0;
    background: linear-gradient(180deg, var(--red) 0%, var(--red-deep) 100%);
  }
  .band-top { top: 0; height: 30px; }
  .band-bottom { bottom: 0; height: 37px; background: linear-gradient(0deg, var(--red-deep) 0%, var(--red) 100%); }
  .title-bar {
    position: absolute; top: 30px; left: 0; right: 0; height: 41px;
    background: linear-gradient(180deg, var(--title-bar) 0%, var(--title-bar-dark) 100%);
    display: flex; align-items: center; padding: 0 28px;
    color: var(--white); font-size: 22px; letter-spacing: 0.2px;
    text-transform: uppercase;
  }
  .page--right .title-bar { justify-content: flex-end; }
  .title-bar strong { font-weight: 800; margin-right: 7px; }
  .title-bar span { font-weight: 300; }
  .photo {
    position: absolute; top: 71px; left: 0; right: 0; height: 410px;
  }
  .photo--meeting {
    background: linear-gradient(115deg, #f3f1ee 0%, #dcd7d0 35%, #c9c4be 55%, #eceae6 75%, #b9b2a8 100%);
  }
  .photo--sandwich {
    background: radial-gradient(ellipse at 70% 50%, #d8b07a 0%, #a57a48 22%, #2c3f6b 48%, #16203a 75%, #0d1220 100%);
  }
  .info-bar {
    position: absolute; top: 481px; left: 0; right: 0; height: 52px;
    background: var(--info-bar);
    display: flex; align-items: center;
  }
  .brand-panel {
    width: 92px; height: 52px; margin-left: 14px; margin-top: -14px;
    background: var(--red);
    display: flex; align-items: center; justify-content: center;
    color: var(--white); font-weight: 600; font-size: 13px;
    align-self: flex-start; padding-top: 0;
  }
  .page--right .brand-panel { margin-left: 14px; }
  .tagline { margin-left: 12px; flex: 1; color: var(--white); }
  .tagline p { font-size: 10.5px; font-weight: 300; line-height: 1.25; }
  .tagline small { display: block; font-size: 7px; color: var(--muted); margin-top: 2px; line-height: 1.3; }
  .price {
    display: flex; align-items: flex-start; color: var(--orange);
    margin-right: 18px; margin-top: -22px;
  }
  .price .currency { font-size: 24px; font-weight: 300; margin-top: 20px; margin-right: 2px; }
  .price .amount { font-size: 50px; font-weight: 800; line-height: 1; letter-spacing: -1px; }
  .price .per { font-size: 10px; font-weight: 400; line-height: 1.15; margin-left: 4px; margin-top: 6px; text-transform: uppercase; }
  .content {
    position: absolute; top: 544px; left: 12px; right: 12px; height: 150px;
    display: flex; gap: 6px;
  }
  .content-box {
    background: var(--box-bg); padding: 8px 9px; overflow: hidden;
    font-size: 5.8px; line-height: 1.45;
  }
  .content-box h2 { font-size: 9px; font-weight: 800; margin-bottom: 5px; letter-spacing: 0.3px; }
  .content-box h3 { font-size: 6px; font-weight: 700; margin-top: 4px; }
  .content-box p { margin-bottom: 2px; }
  .page--left .features { width: 174px; }
  .page--left .details { width: 172px; }
  .page--left .accessories { flex: 1; }
  .page--right .features { width: 150px; }
  .page--right .details { width: 182px; }
  .page--right .accessories { flex: 1; }
  .accessory-photo {
    background: linear-gradient(135deg, #f5efe6 0%, #8a5a34 50%, #3b2414 100%);
    height: 58px; margin-bottom: 6px;
  }
  .machine-row { display: flex; gap: 6px; }
  .machine-tile {
    flex: 1; height: 58px; border: 1px solid #cfcfcf; background: var(--white);
    display: flex; align-items: center; justify-content: center;
  }
  .machine-shot {
    width: 60%; height: 80%;
    background: linear-gradient(180deg, #5a5a5e 0%, #1d1d20 60%, #3a3a3e 100%);
  }
  .page--right .accessories .machine-row { margin-top: 6px; }
  .page--right .accessories .machine-tile { height: 64px; }
</style>
</head>
<body>
<main class="spread">

  <section class="page page--left">
    <div class="band-top"></div>
    <header class="title-bar"><strong>Whole Company</strong><span>Solution</span></header>
    <div class="photo photo--meeting" role="img" aria-label="Colleagues in a bright office meeting with coffee on the table"></div>
    <div class="info-bar">
      <div class="brand-panel">Brewvanta</div>
      <div class="tagline">
        <p>The Corporate Office Partner in Automatic Coffee Making.</p>
        <small>Dimensions – Brewvanta machine<br>W: 375 D: 560 H: 818</small>
      </div>
      <div class="price"><span class="currency">$</span><span class="amount">24</span><span class="per">Per<br>Day</span></div>
    </div>
    <div class="content">
      <article class="content-box features">
        <h2>FEATURES</h2>
        <h3>Fresh Coffee – Bean to Cup Brew</h3>
        <p>Every cup is ground and brewed on demand for rich flavour, crema and aroma across your whole workplace.</p>
        <h3>Fully Automated Cleaning Program</h3>
        <p>Daily rinse cycles keep every component hygienic with no effort from your staff.</p>
      </article>
      <article class="content-box details">
        <h3>Easy Operation – Graphic Display</h3>
        <p>Choose from thirty beverages with a single touch on the clear colour screen, built for busy teams.</p>
        <h3>Automatic Coffee Quality System</h3>
        <p>Constant monitoring of grind and temperature keeps every cup consistent.</p>
        <h3>Choices</h3>
        <p>Strength and volume can be set for small, medium and large cups to suit every taste.</p>
      </article>
      <aside class="content-box accessories">
        <div class="accessory-photo" role="img" aria-label="Roasted coffee beans beside a cup"></div>
        <div class="machine-row">
          <div class="machine-tile"><div class="machine-shot" role="img" aria-label="Automatic coffee machine"></div></div>
          <div class="machine-tile"><div class="machine-shot" role="img" aria-label="Automatic coffee machine with accessory"></div></div>
        </div>
      </aside>
    </div>
    <div class="band-bottom"></div>
  </section>

  <section class="page page--right">
    <div class="band-top"></div>
    <header class="title-bar"><strong>Food Service</strong><span>Solution</span></header>
    <div class="photo photo--sandwich" role="img" aria-label="Hand holding a fresh baguette sandwich"></div>
    <div class="info-bar">
      <div class="brand-panel">Brewvanta</div>
      <div class="tagline">
        <p>The Corporate Office Partner in Automatic Coffee Making.</p>
        <small>Dimensions – Brewvanta machine<br>W: 375 D: 560 H: 818</small>
      </div>
      <div class="price"><span class="currency">$</span><span class="amount">28</span><span class="per">Per<br>Day</span></div>
    </div>
    <div class="content">
      <article class="content-box features">
        <h2>FEATURES</h2>
        <h3>Fresh Coffee</h3>
        <p>At the push of a button the machine grinds and brews a full bodied cup in seconds.</p>
        <h3>Fresh Milk – Cool Milk Frothing</h3>
        <p>Silky milk foam is dispensed straight into the cup at the ideal temperature.</p>
        <h3>Fully Automated Cleaning Program</h3>
        <p>Rinsing and cleaning run on a timer so parts stay hygienic all day.</p>
      </article>
      <article class="content-box details">
        <h3>Easy Operation – Graphic Display</h3>
        <p>Twenty four drinks are shown as clear icons so anyone can serve themselves quickly.</p>
        <h3>Chocolate Module (Optional)</h3>
        <p>Add a hot chocolate canister for rich cocoa and mocha beverages on demand.</p>
        <h3>Choices</h3>
        <p>Set strength, volume and temperature for every drink on the menu.</p>
        <h3>Energy Saver – Eco Mode</h3>
      </article>
      <aside class="content-box accessories">
        <p>Patented technology to ensure top energy savings and low running costs for your site.</p>
        <h3>Connectivity – Telemetry</h3>
        <p>Reports machine status and stock levels so refills arrive before you run out.</p>
        <div class="machine-row">
          <div class="machine-tile"><div class="machine-shot" role="img" aria-label="Automatic coffee machine"></div></div>
          <div class="machine-tile"><div class="machine-shot" role="img" aria-label="Automatic coffee machine with milk unit"></div></div>
        </div>
      </aside>
    </div>
    <div class="band-bottom"></div>
  </section>

</main>
</body>
</html>
```